Quiet Harbor
How Opening the Palate Renews Rest, Vigor, and Poise Without an Operation
Creative Brief
Description: I’m seeking a talented designer to create a professional, simple, and wellness-oriented cover for my upcoming book. The book explores the hidden connection between jaw expansion, airway health, and whole-body wellness. What I’m Looking For: Clean, minimalist style (similar to Tidal by Colin Marsby and The Lumen Method by Gregory Tallisant). A design that communicates both trustworthiness and transformation — this is a serious wellness/health book, not a textbook. Imagery that subtly conveys space, breathing, and expansion (abstract or symbolic — not literal medical images). Professional typography with good spacing and balance. A design that looks credible in both print and digital formats (Amazon, bookstore, audiobook). Deliverables: Front cover design (with title, subtitle, author name). Full jacket design (front, spine, back cover with provided text). Final files in print-ready PDF + high-res PNG/JPEG + source files (AI/PSD/INDD). About the Author: Dr. Darren Okafield, DMD, is a board-certified orthodontist and dentofacial orthopedist recognized internationally for his airway-focused approach. Featured in Plain Ease, Vantage Wellbeing, and BX Magazine, he helps patients achieve healthier smiles and better breathing without unnecessary surgery.
Health
Health minded people. Men and women but maybe lean a little more toward women
Design the front and back cover. Attached is a current design but I want to go with a new title subtitle of: Title: Open Passage Subtitle: The Quiet Link Among Inhaling, Rest, and Total Vitality ... I'm also open to other titles that might convey a similar message. Here is the back of the book description: What if the cause of your fatigue, poor sleep, anxiety, or lack of focus wasn’t in your mind—but in your mouth? Hidden jaw and airway problems affect millions of adults, yet most go undiagnosed. A narrow palate, mouth breathing, or underdeveloped jaws can quietly disrupt your health, appearance, and energy every single day. In this groundbreaking book, Dr. Darren Okafield—board-certified orthodontist, dentofacial orthopedist, airway-focused clinician, and author of The Kolvex Principle—reveals how your smile, facial balance, and airway are deeply connected to whole-body health. Through real patient stories, simple science, and clear explanations of modern treatment approaches, you’ll discover: The hidden epidemic of underdeveloped jaws and how it impacts breathing, sleep, wellness, and facial harmony Why mouth breathing is more than a bad habit—it’s a health disruptor The truth about palate expanders for adults and children (and what’s important to know about them) What to expect on your treatment journey, from first consultation to long-term results How better breathing can transform not only your health—but also your confidence and overall vitality This isn’t just about teeth. It’s about unlocking the power of proper breathing, creating balance in the face, and giving your body the space it needs to thrive. If you’ve ever felt like something was “off” with your health but couldn’t find the root cause, this book offers the missing link—and a guide to lasting transformation. About the Author Dr. Darren Okafield is a board-certified orthodontist and dentofacial orthopedist and founder of TrelbyBraceClinic.example. Recognized internationally for his airway-focused approach, he helps children, teens, and adults achieve healthier smiles and better breathing without unnecessary surgery. Featured in Plain Ease, Vantage Wellbeing, and with an upcoming expert feature in BX Magazine, he is passionate about educating both consumers and professionals on the life-changing connection between orthodontics, facial development, and whole-body health.

```html
<!DOCTYPE html>
<html lang="en">
<head>
<meta charset="utf-8">
<title>Open Passage — Front Cover</title>
<link rel="stylesheet" href="https://fonts.googleapis.com/css2?family=Cormorant+Garamond:wght@400;500&family=Montserrat:wght@500&display=swap">
<style>
  :root {
    --page-bg: #e9e7e3;
    --cover-top: #f4faf7;
    --cover-mid: #d3efe6;
    --cover-bottom: #a9e2d6;
    --title-ink: #6e8b8a;
    --subtitle-ink: #2f7d7b;
    --author-ink: #4f8584;
    --emblem-core: #7fcfc3;
    --emblem-glow: rgba(143, 214, 202, 0.25);
  }
  * { box-sizing: border-box; margin: 0; padding: 0; }
  html, body {
    width: 1200px;
    height: 901px;
    overflow: hidden;
    background: var(--page-bg);
  }
  .stage {
    width: 1200px;
    height: 901px;
    display: flex;
    align-items: center;
    justify-content: center;
  }
  .book-cover {
    position: relative;
    width: 560px;
    height: 840px;
    background: linear-gradient(175deg, var(--cover-top) 0%, var(--cover-mid) 45%, var(--cover-bottom) 100%);
    box-shadow: 0 10px 30px rgba(0, 0, 0, 0.12);
    text-align: center;
  }
  .cover-title {
    position: absolute;
    top: 92px;
    left: 0;
    right: 0;
    font-family: "Cormorant Garamond", serif;
    font-weight: 400;
    font-size: 66px;
    line-height: 1.02;
    letter-spacing: 0.2em;
    padding-left: 0.2em;
    color: var(--title-ink);
    text-transform: uppercase;
  }
  .cover-emblem {
    position: absolute;
    top: 260px;
    left: 50%;
    width: 200px;
    height: 200px;
    margin-left: -100px;
    border-radius: 50%;
    background: radial-gradient(circle, var(--emblem-core) 0%, var(--emblem-core) 38%, var(--emblem-glow) 62%, rgba(143, 214, 202, 0) 72%);
  }
  .cover-subtitle {
    position: absolute;
    top: 492px;
    left: 60px;
    right: 60px;
    font-family: "Montserrat", sans-serif;
    font-weight: 500;
    font-size: 17px;
    line-height: 1.45;
    color: var(--subtitle-ink);
  }
  .cover-author {
    position: absolute;
    top: 600px;
    left: 0;
    right: 0;
    font-family: "Cormorant Garamond", serif;
    font-weight: 500;
    font-size: 25px;
    line-height: 1.2;
    letter-spacing: 0.08em;
    color: var(--author-ink);
    text-transform: uppercase;
  }
</style>
</head>
<body>
  <main class="stage">
    <article class="book-cover">
      <h1 class="cover-title">Open<br>Passage</h1>
      <div class="cover-emblem" role="img" aria-label="Profile silhouette of a head surrounded by radiating sunburst lines, symbolising open breathing"></div>
      <p class="cover-subtitle">The Quiet Link Among<br>Inhaling, Rest, and Total Vitality</p>
      <p class="cover-author">Dr. Darren<br>Okafield, DMD</p>
    </article>
  </main>
</body>
</html>
```